Spray Foam Company Business Card

We need a business card designed for our spray foam insulation and roof coatings business. We handle residential and commercial projects.
Construction
We would like it to say:
R & K Spray
with these bullet points
-foam insulation
-waterproofing roof system
-water proofing foundation systems
website is rksprayfoaminsulation.example (this was just purchased)
office phone : 630-482-9164
And 3 cards with names on them the names are :
Derek Halvorsen
Curtis Pennington
Rob Stallworth
maybe the bullet points can go on the back?
if you go this website it is another division of our company and you can see the font we use in the R & K. We do not want to use the same half circles that it has just the lettering
www.coatedrightforyears.example

```html
<!DOCTYPE html>
<html lang="en">
<head>
<meta charset="utf-8">
<title>R &amp; K Spray – Business Cards</title>
<link href="https://fonts.googleapis.com/css2?family=Open+Sans:wght@400;600;700&display=swap" rel="stylesheet">
<style>
  :root {
    --backdrop: #ebe8e3;
    --card-grey: #a8a9ab;
    --navy: #0b1438;
    --red: #c8262d;
    --light-text: #d9dadc;
    --ink: #0b1438;
  }
  * { margin: 0; padding: 0; box-sizing: border-box; }
  html, body {
    width: 1200px; height: 784px; overflow: hidden;
    background: var(--backdrop);
    font-family: "Open Sans", sans-serif;
  }
  .stage {
    position: relative; width: 1200px; height: 784px;
    display: flex; align-items: center; justify-content: center; gap: 50px;
  }
  .card {
    position: relative; width: 540px; height: 309px;
    background: var(--card-grey);
    overflow: hidden;
    box-shadow: 0 6px 18px rgba(0,0,0,.18);
  }
  .card-shape { position: absolute; inset: 0; width: 540px; height: 309px; }

  /* back side */
  .services { position: absolute; left: 40px; top: 62px; list-style: none; }
  .services li {
    font-size: 13px; letter-spacing: 1.2px; text-transform: uppercase;
    color: var(--light-text); margin-bottom: 28px;
  }
  .services li.highlight { color: var(--red); }
  .brand-back {
    position: absolute; right: 14px; top: 124px;
    font-size: 26px; font-weight: 700; color: var(--navy);
  }

  /* front side */
  .brand-front {
    position: absolute; left: 48px; top: 42px;
    font-size: 46px; font-weight: 700; color: var(--navy);
  }
  .person {
    position: absolute; left: 40px; top: 178px;
    font-size: 24px; font-weight: 600; color: var(--red);
  }
  .contact { position: absolute; left: 40px; top: 218px; list-style: none; }
  .contact li { display: flex; align-items: center; gap: 8px; color: var(--ink); }
  .contact .phone { font-size: 23px; margin-bottom: 4px; }
  .contact .web { font-size: 16px; }
  .contact svg { flex: none; }
</style>
</head>
<body>
<main class="stage">

  <section class="card card-back" aria-label="Card back">
    <svg class="card-shape" viewBox="0 0 540 309" aria-hidden="true">
      <polygon fill="var(--red)" points="0,0 490,0 478,22 484,36 470,52 476,66 462,82 466,98 452,112 456,128 442,144 446,160 432,174 436,192 420,206 424,222 410,238 412,254 398,268 400,286 388,298 390,309 0,309"/>
      <polygon fill="var(--navy)" points="0,0 470,0 462,18 468,30 455,44 460,60 446,75 451,92 438,106 442,124 428,138 433,156 418,170 423,188 408,202 412,220 398,234 402,252 388,266 391,284 378,296 380,309 0,309"/>
    </svg>
    <ul class="services">
      <li>Water proofing foundation systems</li>
      <li class="highlight">Waterproofing roof system</li>
      <li>Foam insulation</li>
    </ul>
    <div class="brand-back">R &amp; K</div>
  </section>

  <section class="card card-front" aria-label="Card front">
    <svg class="card-shape" viewBox="0 0 540 309" aria-hidden="true">
      <polygon fill="var(--navy)" points="392,0 540,0 540,309 322,309 326,296 337,282 333,264 344,250 340,232 351,218 347,200 358,186 354,168 366,152 361,136 372,122 368,104 379,90 374,74 386,58 380,44 392,28 386,16"/>
      <polygon fill="var(--red)" points="401,0 540,0 540,309 331,309 335,296 346,282 342,264 353,250 349,232 360,218 356,200 367,186 363,168 375,152 370,136 381,122 377,104 388,90 383,74 395,58 389,44 401,28 395,16"/>
    </svg>
    <div class="brand-front">R &amp; K</div>
    <h1 class="person">Derek Halvorsen</h1>
    <ul class="contact">
      <li class="phone">
        <svg width="18" height="18" viewBox="0 0 24 24" aria-hidden="true"><path fill="var(--red)" d="M6.6 10.8a15.1 15.1 0 0 0 6.6 6.6l2.2-2.2c.3-.3.7-.4 1-.2 1.1.4 2.3.6 3.6.6.6 0 1 .4 1 1V20c0 .6-.4 1-1 1A17 17 0 0 1 3 4c0-.6.4-1 1-1h3.5c.6 0 1 .4 1 1 0 1.3.2 2.5.6 3.6.1.3 0 .7-.2 1z"/></svg>
        630-482-9164
      </li>
      <li class="web">
        <svg width="16" height="16" viewBox="0 0 24 24" aria-hidden="true" fill="none" stroke="var(--red)" stroke-width="2"><circle cx="12" cy="12" r="10"/><path d="M2 12h20M12 2c3 3 3 17 0 20M12 2c-3 3-3 17 0 20"/></svg>
        rksprayfoaminsulation.example
      </li>
    </ul>
  </section>

</main>
</body>
</html>
```